Tov Fest Falcons

We are party planning business. We are a team of established individuals and business in party stream businesses like DJ, Caterers, Party supplies, Kids parties, Events & Private Parties and much more. So basically me and business collaborate a team of business or individuals to do clients party in the best way possible.

Target Market(s)

majority of them 16 to 30 -60% to 70 % and 30 to 40 year olds- 30% to 40 %

Industry/Entity Type

Party Planning

Contact Information for Business Card

Tov
Owner & Manager
0481927354
tovfestfalcons@mailbright.example

Requirements
Must have
• front side : Logo and list of services we provide
DJ's, Catering,All party supplies, Tinyvolta and more...just to show what the business is about when anyone looks at the card and at the rear side my details which are already provided.
Should not have
• Dont make it look we do kids party which is just one of the things we do but don't make my business card look like kids party specialist make it more connecting to youngsters and older crowd more

```html
<!DOCTYPE html>
<html lang="en">
<head>
<meta charset="utf-8">
<title>Tov Fest Falcons — Business Card</title>
<link href="https://fonts.googleapis.com/css2?family=Cinzel:wght@400;700;900&family=Courier+Prime:wght@400;700&display=swap" rel="stylesheet">
<style>
  :root {
    --stage-light: #d9d9d9;
    --stage-dark: #4a4a4a;
    --card: #ffffff;
    --ink: #111111;
    --red: #e0282e;
    --note: #1a1a1a;
    --faint: #f1e2de;
  }
  * { box-sizing: border-box; margin: 0; padding: 0; }
  html, body { width: 1200px; height: 900px; overflow: hidden; }
  body {
    background: radial-gradient(ellipse at 50% 45%, var(--stage-light) 0%, #a9a9a9 55%, var(--stage-dark) 100%);
    position: relative;
  }
  .card {
    position: absolute;
    left: 250px;
    width: 700px;
    height: 390px;
    background: var(--card);
    border-radius: 26px;
    box-shadow: 0 18px 40px rgba(0,0,0,.35);
    overflow: hidden;
  }
  .card--front { top: 40px; }
  .card--back { top: 470px; }

  /* Front */
  .front-name {
    position: absolute;
    left: 60px; top: 140px;
    width: 300px;
    font-family: "Cinzel", serif;
    font-weight: 900;
    font-size: 44px;
    line-height: 1.05;
    color: var(--red);
  }
  .front-mark {
    position: absolute;
    right: 30px; top: 190px;
    width: 180px; height: 180px;
    border-radius: 50%;
    background: var(--faint);
    opacity: .6;
  }
  .services {
    position: absolute;
    left: 430px; top: 60px;
    width: 240px;
    text-align: center;
    font-family: "Cinzel", serif;
  }
  .services__title {
    font-size: 26px;
    font-weight: 700;
    letter-spacing: 1px;
    color: var(--ink);
    margin-bottom: 6px;
  }
  .services__list { list-style: none; position: relative; }
  .services__list li {
    font-size: 14px;
    letter-spacing: 1px;
    line-height: 1.5;
    color: var(--red);
    text-transform: uppercase;
  }
  .services__list .services__more { font-size: 19px; }

  /* Back */
  .logo-block {
    position: absolute;
    left: 30px; top: 50px;
    width: 300px;
    text-align: center;
  }
  .logo-block__circle {
    width: 70px; height: 70px;
    border-radius: 50%;
    background: var(--red);
    margin: 0 auto 14px;
  }
  .logo-block__name {
    font-family: "Cinzel", serif;
    font-weight: 900;
    font-size: 38px;
    line-height: 1.05;
    color: var(--red);
  }
  .logo-block__tagline {
    margin-top: 12px;
    font-family: "Cinzel", serif;
    font-weight: 700;
    font-size: 16px;
    line-height: 1.25;
    color: var(--ink);
  }
  .contact {
    position: absolute;
    left: 355px; top: 150px;
    width: 320px;
    font-family: "Courier Prime", monospace;
  }
  .contact__name { font-size: 34px; font-weight: 700; color: var(--ink); letter-spacing: 2px; line-height: 1.1; }
  .contact__role { font-size: 15px; color: var(--red); margin-bottom: 8px; }
  .contact__line { font-size: 13px; line-height: 1.6; color: var(--ink); font-weight: 700; white-space: nowrap; }
  .contact__line span { color: var(--red); font-weight: 400; }
  .note {
    position: absolute;
    width: 26px; height: 34px;
    border-radius: 8px;
    background: var(--note);
    opacity: .85;
  }
</style>
</head>
<body>
  <section class="card card--front" aria-label="Card front">
    <div class="front-mark" role="img" aria-label="Faint brand decoration"></div>
    <h1 class="front-name">Tov Fest Falcons</h1>
    <div class="services">
      <h2 class="services__title">OUR SERVICE</h2>
      <ul class="services__list">
        <li>Caterers</li>
        <li>Party Supplies</li>
        <li>Kids Parties</li>
        <li>DJ</li>
        <li>Events &amp; Private Parties</li>
        <li class="services__more">and much more</li>
      </ul>
    </div>
  </section>

  <section class="card card--back" aria-label="Card back">
    <div class="logo-block">
      <div class="logo-block__circle"></div>
      <div class="logo-block__name">Tov Fest Falcons</div>
      <p class="logo-block__tagline">Delivering The Ultimate<br>Treasures To Your Party</p>
    </div>
    <div class="note" style="left:420px; top:28px;" role="img" aria-label="Music note symbol"></div>
    <div class="note" style="left:460px; top:80px; width:20px; height:26px;" role="img" aria-label="Music note symbol"></div>
    <div class="note" style="left:630px; top:95px; width:36px; height:54px;" role="img" aria-label="Treble clef symbol"></div>
    <div class="note" style="left:385px; top:300px;" role="img" aria-label="Treble clef symbol"></div>
    <div class="note" style="left:600px; top:320px; width:50px; height:28px;" role="img" aria-label="Music notes symbol"></div>
    <div class="contact">
      <div class="contact__name">TOV</div>
      <div class="contact__role">Owner &amp; Manager</div>
      <div class="contact__line">phone: <span>0481927354</span></div>
      <div class="contact__line">email: <span>tovfestfalcons@mailbright.example</span></div>
    </div>
  </section>
</body>
</html>
```